Carte d'affaire bilingue

Nous avons besoin d'une carte d'affaire pour notre entreprise spécialisée en vente et achat de terrain. Nous sommes une agence immobilière et nous voulons une carte avec le recto en Français et le verso en anglais. Nous voulons une image sobre et épurée. Nous avons de la clientèle internationale et nous voulons une carte très professionnelle mais qui se démarque. Nous voulons cibler une clientèle commerciale, industrielle, contracteurs et promoteurs immobiliers.

Hi everybody, we saw all your conception and we are approching of what we like but the "WOW" is missing.

We love the little sign to specify (phone or email) but we can put them in a square to make like our logo, we love also dark gray not lite gray, we also love the stainless lines. In our logo you can see a little sign +. For us is signyfy " Always further" so if you can put many little +++++ in the conception somewhere very discret it will be appreciate. We also like a kind of round that make a magnyfying glass, because we search land we found opportunity.

Thank you

Reason: I ask different things in the last day but no one do what i am asking for. For the conception # 3016702 that we love we ask changes.

We like simplicity, urban design, corporate, international. The card must have one side in french and the other side in english. We like dark gray,silver, and a little bit of green.

Target Market(s)

Investors, developers, construction builders, etc...

Font styles to use
Serif
Sans Serif

Requirements
Must have
• logo
La mention: Agence immobilière (Francais) / Real Estate Agency (anglais)
Sous le nom: Courtier immobilier agréé (Français) / Real Estate Broker

```html
<!DOCTYPE html>
<html lang="fr">
<head>
<meta charset="utf-8">
<title>Terrain Horizon – Cartes d'affaires</title>
<link rel="stylesheet" href="https://fonts.googleapis.com/css2?family=Cinzel:wght@500&family=Lato:wght@400;700&display=swap">
<style>
  :root {
    --bg: #cfd0d1;
    --card: #ffffff;
    --ink: #3a3b3d;
    --ink-soft: #5b5c5f;
    --green: #0f8a3c;
    --green-dark: #0a6b2d;
    --silver-light: #f1f1f1;
    --silver: #c4c5c7;
    --silver-dark: #9a9b9d;
    --photo: #c8c9cb;
    --plus: #d9dadb;
  }
  * { box-sizing: border-box; margin: 0; padding: 0; }
  html, body { width: 1200px; height: 823px; overflow: hidden; }
  body {
    background: var(--bg);
    font-family: "Lato", sans-serif;
    color: var(--ink);
    position: relative;
  }
  .card {
    position: absolute;
    top: 256px;
    width: 540px;
    height: 310px;
    background: var(--card);
    overflow: hidden;
    box-shadow: 0 4px 14px rgba(0,0,0,.18);
  }
  .card--fr { left: 40px; }
  .card--en { left: 620px; }

  .brand { position: absolute; left: 24px; top: 24px; display: flex; align-items: center; gap: 12px; }
  .brand__mark { width: 44px; height: 44px; background: var(--green); }
  .brand__name {
    font-family: "Cinzel", serif; font-weight: 500;
    font-size: 30px; letter-spacing: 1px; color: var(--ink);
  }
  .brand__mention {
    position: absolute; right: 170px; top: 76px;
    font-size: 15px; color: var(--ink);
  }
  .rule {
    position: absolute; left: 20px; right: 20px; top: 100px; height: 3px;
    background: linear-gradient(90deg, var(--silver-dark), var(--silver-light) 45%, var(--silver) 70%, var(--silver-light));
  }
  .photo {
    position: absolute; right: 24px; top: 122px; width: 130px; height: 130px;
    background: var(--photo);
  }
  .person { position: absolute; left: 28px; top: 118px; }
  .person__name { color: var(--green); font-size: 18px; font-weight: 700; letter-spacing: .3px; }
  .person__role { font-size: 14px; line-height: 1.2; color: var(--ink); }

  .contacts {
    position: absolute; left: 28px; top: 186px; width: 360px;
    font-size: 13px; color: var(--ink);
    display: grid; grid-template-columns: 170px 190px; row-gap: 6px;
  }
  .contact { display: flex; align-items: center; gap: 5px; white-space: nowrap; }
  .contact--wide { grid-column: 1 / 3; font-size: 12px; }
  .icon { width: 14px; height: 14px; flex: none; background: var(--green); display: block; }

  .band {
    position: absolute; left: 0; right: 0; bottom: 0; height: 38px;
    background: linear-gradient(90deg, var(--silver) 0%, var(--silver-light) 40%, var(--silver) 75%, var(--silver-light));
  }
  .tollfree { position: absolute; left: 24px; bottom: 10px; font-size: 13px; color: var(--ink); }
  .tollfree b { color: var(--green); }
  .web {
    position: absolute; right: 0; bottom: 0; width: 170px; height: 32px;
    background: var(--green); color: #fff; font-size: 14px;
    display: flex; align-items: center; justify-content: flex-end; padding-right: 14px;
  }
  .plus { position: absolute; color: var(--plus); font-size: 22px; line-height: 1; font-weight: 400; }
  .plus--top { right: 14px; top: 10px; }
  .plus--band { right: 178px; bottom: 6px; color: #fff; }
</style>
</head>
<body>

<!-- Recto français -->
<section class="card card--fr" lang="fr">
  <div class="brand"><span class="brand__mark"></span><span class="brand__name">Terrain Horizon</span></div>
  <div class="brand__mention">Agence Immobilière</div>
  <span class="plus plus--top">+</span>
  <div class="rule"></div>
  <div class="photo" role="img" aria-label="Photo de la courtière"></div>
  <div class="person">
    <p class="person__name">MAUDE LAVERGNE</p>
    <p class="person__role">Courtier Immobilier Agréé, D.A.<br>Vice Présidente</p>
  </div>
  <div class="contacts">
    <p class="contact"><svg class="icon" viewBox="0 0 14 14"><rect width="14" height="14" fill="#0f8a3c"/><circle cx="7" cy="7" r="2.3" fill="none" stroke="#fff" stroke-width="1.2"/><path d="M9.3 5v3q0 1.4 1.3 1.1A4 4 0 1 0 9 10.5" fill="none" stroke="#fff" stroke-width="1.2"/></svg>m.lavergne@hzland.com</p>
    <p class="contact"><svg class="icon" viewBox="0 0 14 14"><rect width="14" height="14" fill="#0f8a3c"/><rect x="4.5" y="2.5" width="5" height="9" rx="1" fill="none" stroke="#fff" stroke-width="1.1"/></svg>514-555-0163</p>
    <p class="contact contact--wide"><svg class="icon" viewBox="0 0 14 14"><rect width="14" height="14" fill="#0f8a3c"/><path d="M7 12 4 7.5a3 3 0 1 1 6 0Z" fill="#fff"/><circle cx="7" cy="6" r="1.1" fill="#0f8a3c"/></svg>12 B, Boul. des Érables, 2E, Laval, Qc, H7A 1B2</p>
    <p class="contact"><svg class="icon" viewBox="0 0 14 14"><rect width="14" height="14" fill="#0f8a3c"/><path d="M4 3h2l1 2.3-1.2.9a6 6 0 0 0 2.6 2.6l.9-1.2L11.6 8.6V10.6Q11 11.6 9.5 11.3A8 8 0 0 1 3 4.6Q3 3.3 4 3Z" fill="#fff"/></svg>514-555-0142</p>
    <p class="contact"><svg class="icon" viewBox="0 0 14 14"><rect width="14" height="14" fill="#0f8a3c"/><rect x="3" y="6" width="8" height="5" fill="#fff"/><rect x="4.5" y="2.5" width="5" height="3.5" fill="none" stroke="#fff" stroke-width="1"/></svg>450-555-0187</p>
  </div>
  <div class="band"></div>
  <p class="tollfree"><b>Toll Free:</b> 1-866-HORIZON</p>
  <span class="plus plus--band">+</span>
  <div class="web">www.HZLAND.com</div>
</section>

<!-- Verso anglais -->
<section class="card card--en" lang="en">
  <div class="brand"><span class="brand__mark"></span><span class="brand__name">Horizon Land</span></div>
  <div class="brand__mention">Real Estate Agency</div>
  <span class="plus plus--top">+</span>
  <div class="rule"></div>
  <div class="photo" role="img" aria-label="Portrait of the broker"></div>
  <div class="person">
    <p class="person__name">MAUDE LAVERGNE</p>
    <p class="person__role">Real Estate Broker, D.A.<br>Vice President</p>
  </div>
  <div class="contacts">
    <p class="contact"><svg class="icon" viewBox="0 0 14 14"><rect width="14" height="14" fill="#0f8a3c"/><circle cx="7" cy="7" r="2.3" fill="none" stroke="#fff" stroke-width="1.2"/><path d="M9.3 5v3q0 1.4 1.3 1.1A4 4 0 1 0 9 10.5" fill="none" stroke="#fff" stroke-width="1.2"/></svg>m.lavergne@hzland.com</p>
    <p class="contact"><svg class="icon" viewBox="0 0 14 14"><rect width="14" height="14" fill="#0f8a3c"/><rect x="4.5" y="2.5" width="5" height="9" rx="1" fill="none" stroke="#fff" stroke-width="1.1"/></svg>514-555-0163</p>
    <p class="contact contact--wide"><svg class="icon" viewBox="0 0 14 14"><rect width="14" height="14" fill="#0f8a3c"/><path d="M7 12 4 7.5a3 3 0 1 1 6 0Z" fill="#fff"/><circle cx="7" cy="6" r="1.1" fill="#0f8a3c"/></svg>12 B, Érables Blv., 2E, Laval, Qc, H7A 1B2</p>
    <p class="contact"><svg class="icon" viewBox="0 0 14 14"><rect width="14" height="14" fill="#0f8a3c"/><path d="M4 3h2l1 2.3-1.2.9a6 6 0 0 0 2.6 2.6l.9-1.2L11.6 8.6V10.6Q11 11.6 9.5 11.3A8 8 0 0 1 3 4.6Q3 3.3 4 3Z" fill="#fff"/></svg>514-555-0142</p>
    <p class="contact"><svg class="icon" viewBox="0 0 14 14"><rect width="14" height="14" fill="#0f8a3c"/><rect x="3" y="6" width="8" height="5" fill="#fff"/><rect x="4.5" y="2.5" width="5" height="3.5" fill="none" stroke="#fff" stroke-width="1"/></svg>450-555-0187</p>
  </div>
  <div class="band"></div>
  <p class="tollfree"><b>Toll Free:</b> 1-866-HZLANDS</p>
  <span class="plus plus--band">+</span>
  <div class="web">www.HZLAND.com</div>
</section>

</body>
</html>
```